2021 IT Training Presentation Deck Refresh

Copper Lantern is an IT education services firm. We teach IT industry standards and technologies. We are in need of an updated training presentation deck that factors in a fresh take for:

1) Agenda/Table of Contents
2) Chapter Topic Summary
2) Chapter Introduction and Learning Objectives
3) Chapter Recaps
4) Important Point/Pro Tip emphasis
5) Warning Message
6) Mini Quiz layout
7) Lab Exercise Introduction
7) Deck Close Out

Incorporating the official Copper Lantern colour palette for materials that will likely be used in self-paced/online recorded versions of courses.

Target Market(s)

IT

Industry/Entity Type

Computer Training

Requirements
Nice to have
• placeholder sections for images of IT workers in an office or by a computer

```html
<!DOCTYPE html>
<html lang="en">
<head>
<meta charset="utf-8">
<title>Copper Lantern – Presentation Template</title>
<link href="https://fonts.googleapis.com/css2?family=Roboto:wght@300;400;500;700&family=Barlow+Semi+Condensed:wght@400;500&display=swap" rel="stylesheet">
<style>
  :root{
    --navy:#0b0a45;
    --indigo:#2d2e7a;
    --indigo-2:#34358c;
    --royal:#3557b0;
    --sky:#5b8fd6;
    --sky-soft:#a9c4ee;
    --ice:#e3f0fa;
    --ice-2:#d1e8f5;
    --paper:#f4f4f5;
    --ink:#1c1c55;
    --title-blue:#2e4aa0;
    --accent:#4f7fc4;
    --muted:#7a8ab8;
    --photo-office:linear-gradient(135deg,#4a3d36 0%,#7d6a5c 40%,#b9b2aa 75%,#d8d6d2 100%);
    --photo-cool:linear-gradient(135deg,#8fb6d8 0%,#b9d4ea 50%,#6e93c4 100%);
    --photo-warn:linear-gradient(135deg,#2d3f86 0%,#3e63b0 55%,#6a94d2 100%);
  }
  *{box-sizing:border-box;margin:0;padding:0}
  html,body{width:1200px;height:2194px;overflow:hidden;background:#fff}
  body{position:relative;font-family:"Roboto",Arial,sans-serif;color:var(--ink)}

  /* header */
  .board-brand{position:absolute;left:94px;top:112px;width:280px;height:130px}
  .board-brand .mark-dot{position:absolute;left:112px;top:0;width:52px;height:52px;border-radius:50%;background:var(--accent)}
  .board-brand .name{position:absolute;left:0;top:72px;font-weight:300;font-size:41px;color:var(--accent);white-space:nowrap}
  .board-title{position:absolute;left:424px;top:142px;font-family:"Barlow Semi Condensed","Roboto",sans-serif;font-weight:500;font-size:52px;letter-spacing:4px;white-space:nowrap}
  .board-title .dark{color:var(--ink)}
  .board-title .light{color:var(--accent)}

  /* slide grid */
  .slide{position:absolute;width:361px;height:203px;overflow:hidden;box-shadow:0 6px 16px rgba(20,20,60,.28)}
  .col-a{left:33px}.col-b{left:422px}.col-c{left:806px}
  .row-1{top:303px}.row-2{top:563px}.row-3{top:823px}.row-4{top:1083px}.row-5{top:1342px}.row-6{top:1602px}.row-7{top:1862px}
  .slide > *{position:absolute}
  .bg-navy{background:var(--navy)}
  .bg-ice{background:var(--ice)}
  .bg-paper{background:var(--paper)}
  .bg-royal{background:var(--royal)}
  .bg-indigo{background:var(--indigo)}

  .photo{background:var(--photo-office)}
  .photo.cool{background:var(--photo-cool)}
  .photo.warn{background:var(--photo-warn)}

  .brand-tag{top:8px;right:9px;display:flex;align-items:center;gap:3px;font-size:5.5px;font-weight:500;color:var(--accent);white-space:nowrap}
  .brand-tag::before{content:"";width:6px;height:6px;border-radius:50%;background:currentColor}
  .brand-tag.on-dark{color:var(--sky-soft)}
  .footer-url{left:15px;bottom:6px;font-size:3.6px;color:var(--sky)}
  .page-no{right:10px;bottom:6px;font-size:3.6px;color:var(--sky)}

  .slide-title{font-weight:300;text-transform:uppercase;line-height:1.02}
  .sub-label{font-size:4.2px;font-weight:700;text-transform:uppercase;color:var(--ink)}
  .lorem{font-size:3.7px;line-height:1.38;text-align:justify;color:var(--ink)}
  .on-dark .lorem,.lorem.light{color:#fff}
  .lorem.soft{color:var(--sky)}

  .num-dot{display:flex;align-items:center;justify-content:center;width:20px;height:20px;border-radius:50%;background:var(--indigo);color:#fff;font-size:6px;border:2px solid #c8d6f0;flex:none}
  .num-dot.light{background:var(--sky)}
  .item{display:flex;gap:9px;align-items:flex-start}
  .item .copy{width:100px}
  .item .copy .sub-label{font-size:3.6px;margin-bottom:2px}
  .item .copy .lorem{font-size:3.4px}

  /* covers */
  .cover-art{left:72px;top:30px;width:220px;height:98px;border-radius:50px 60px 30px 40px}
  .cover-title{left:0;width:100%;top:146px;text-align:center;font-weight:500;font-size:10.6px}
  .cover-tag{left:0;width:100%;top:160px;text-align:center;font-size:5px;text-transform:uppercase}

  /* toc */
  .toc-title{left:58px;top:82px;font-size:17px;line-height:1.05;text-align:center}
  .toc-title .a{color:var(--accent)}
  .toc-title .b{color:var(--sky-soft)}
  .toc-list{left:211px;top:17px;list-style:none}
  .toc-list li{display:flex;align-items:center;gap:8px;height:24.6px}
  .toc-list .n{font-style:italic;font-weight:300;font-size:13px;color:var(--sky)}
  .toc-list .t{font-size:5.4px;color:#fff}
  .toc-list .s{display:block;font-size:3px;color:var(--sky)}

  .divider{height:.6px;background:var(--sky)}

  /* numbered grid */
  .obj-cell{width:80px;text-align:center}
  .obj-cell .n{font-size:7px;color:var(--sky)}
  .obj-cell .sub-label{color:var(--sky);font-size:3.5px;margin:5px 0 3px}
  .obj-cell .lorem{color:#fff;text-align:center;font-size:3.6px}

  /* quiz */
  .quiz-cell{display:flex;gap:10px;width:100px}
  .quiz-cell .n{font-size:6px;color:#fff}
  .quiz-cell .q{font-size:3.5px;color:var(--sky);font-weight:500;margin-bottom:1px}
  .quiz-cell .lorem{color:#fff;font-size:3.4px;text-align:left}
</style>
</head>
<body>

<header>
  <div class="board-brand">
    <span class="mark-dot"></span>
    <span class="name">Copper Lantern</span>
  </div>
  <h1 class="board-title"><span class="dark">PRESENTATION</span> <span class="light">TEMPLATE</span></h1>
</header>

<main>

<!-- 1 cover dark -->
<section class="slide col-a row-1 bg-navy">
  <div class="cover-art photo" role="img" aria-label="Classroom photo of IT learners at computers"></div>
  <h2 class="cover-title" style="color:#fff">COPPER LANTERN IT EDUCATION SERVICES</h2>
  <p class="cover-tag" style="color:#fff">We teach IT industry standards and technologies.</p>
  <span class="footer-url">www.copperlantern-learn.net</span>
</section>

<!-- 2 cover light -->
<section class="slide col-b row-1 bg-ice">
  <div class="cover-art photo" role="img" aria-label="Classroom photo of IT learners at computers"></div>
  <h2 class="cover-title">COPPER LANTERN IT EDUCATION SERVICES</h2>
  <p class="cover-tag">We teach IT industry standards and technologies.</p>
  <span class="footer-url">www.copperlantern-learn.net</span>
</section>

<!-- 3 toc -->
<section class="slide col-c row-1 bg-navy">
  <span class="brand-tag on-dark" style="left:14px;right:auto">Copper Lantern</span>
  <h2 class="toc-title slide-title"><span class="a">Table of</span><br><span class="b">Contents</span></h2>
  <ol class="toc-list">
    <li><span class="n">01</span><span class="t">Topic Summary<span class="s">Concepts before labs</span></span></li>
    <li><span class="n">02</span><span class="t">Introduction and Learning Objectives<span class="s">Goals for the unit</span></span></li>
    <li><span class="n">03</span><span class="t">Recaps<span class="s">Goals for the unit</span></span></li>
    <li><span class="n">04</span><span class="t">Important Point/Pro Tip emphasis<span class="s">Goals for the unit</span></span></li>
    <li><span class="n">05</span><span class="t">Warning Message<span class="s">Goals for the unit</span></span></li>
    <li><span class="n">06</span><span class="t">Mini Quiz<span class="s">Goals for the unit</span></span></li>
    <li><span class="n">07</span><span class="t">Lab Exercise Introduction<span class="s">Goals for the unit</span></span></li>
  </ol>
  <span class="footer-url">www.copperlantern-learn.net</span>
  <span class="page-no">3</span>
</section>

<!-- 4 topic summary one column -->
<section class="slide col-a row-2 bg-paper">
  <span class="brand-tag">Copper Lantern</span>
  <h2 class="slide-title" style="left:30px;top:31px;font-size:14px;color:var(--title-blue)">Topic<br>Summary<br>One<br>Column</h2>
  <div class="divider" style="left:30px;top:103px;width:105px"></div>
  <p class="sub-label" style="left:30px;top:107px">Subtitle Example</p>
  <p class="lorem" style="left:30px;top:117px;width:105px">Lorem ipsum dolor sit amet, consectetur adipiscing elit. Fusce diam tortor, mattis quis dapibus vitae, euismod non purus. Maecenas ut lacus nec mauris feugiat tristique et in metus. Duis congue eros vel lectus semper semper. Nullam finibus nisl ut ligula.</p>
  <p class="lorem" style="left:143px;top:48px;width:190px">Lorem ipsum dolor sit amet, consectetur adipiscing elit. Fusce diam tortor, mattis quis dapibus vitae, euismod non purus. Maecenas ut lacus nec mauris feugiat tristique et in metus. Duis congue eros vel lectus semper semper. Nullam finibus nisl ut ligula vestibulum, ut semper ex suscipit. Cras fringilla suscipit cursus. Aenean accumsan malesuada hendrerit. Morbi sit amet dolor ante. Duis quis viverra urna, in ultricies diam. Morbi sodales volutpat tellus, quis aliquam urna cursus et. Proin commodo arcu nec nisl rhoncus dapibus. Praesent nec elit non metus mollis placerat. Vivamus porta pulvinar iaculis. Donec augue arcu, volutpat nec risus eget, finibus lacinia ligula. Curabitur bibendum arcu sit amet faucibus posuere. Curabitur rhoncus, diam vel congue pulvinar, erat massa lacinia purus, in laoreet purus massa in nunc. Phasellus finibus malesuada lobortis. Sed quis tellus id nulla mollis iaculis. Nam nec auctor arcu. Aenean molestie lacus ut urna accumsan, a rhoncus orci rhoncus. Fusce orci velit, euismod quis pulvinar ac, ultrices vel dui. Praesent commodo, odio eu ullamcorper eleifend, magna metus euismod elit, in porttitor urna nisl ut nulla. Donec accumsan egestas nulla, ut sollicitudin nulla lacinia ac. Pellentesque felis est, tincidunt et suscipit id, rutrum at odio. Sed fringilla porttitor ipsum. Morbi cursus massa eget arcu hendrerit eleifend.</p>
  <span class="footer-url">www.copperlantern-learn.net</span>
  <span class="page-no">4</span>
</section>

<!-- 5 topic summary two columns -->
<section class="slide col-b row-2 bg-paper">
  <span class="brand-tag">Copper Lantern</span>
  <h2 class="slide-title" style="left:30px;top:31px;font-size:14px;color:var(--title-blue)">Topic<br>Summary<br>Two<br>Columns</h2>
  <div class="divider" style="left:30px;top:103px;width:105px"></div>
  <p class="sub-label" style="left:30px;top:107px">Subtitle Example</p>
  <p class="lorem" style="left:30px;top:117px;width:105px">Lorem ipsum dolor sit amet, consectetur adipiscing elit. Fusce diam tortor, mattis quis dapibus vitae, euismod non purus. Maecenas ut lacus nec mauris feugiat tristique et in metus. Duis congue eros vel lectus semper semper. Nullam finibus nisl ut ligula.</p>
  <p class="lorem" style="left:143px;top:48px;width:86px">Lorem ipsum dolor sit amet, consectetur adipiscing elit. Fusce diam tortor, mattis quis dapibus vitae, euismod non purus. Maecenas ut lacus nec mauris feugiat tristique et in metus. Duis congue eros vel lectus semper semper. Nullam finibus nisl ut ligula vestibulum, ut semper ex suscipit. Cras fringilla suscipit cursus. Aenean accumsan malesuada hendrerit. Morbi sit amet dolor ante. Duis quis viverra urna, in ultricies diam. Morbi sodales volutpat tellus, quis aliquam urna cursus et. Proin commodo arcu nec nisl rhoncus dapibus. Praesent nec elit non metus mollis placerat. Vivamus porta pulvinar iaculis. Donec augue arcu, volutpat nec risus eget, finibus lacinia ligula. Curabitur bibendum arcu sit amet faucibus. Curabitur rhoncus, diam vel congue.</p>
  <p class="lorem" style="left:237px;top:48px;width:96px">pulvinar, erat massa lacinia purus, in laoreet purus massa in nunc. Phasellus finibus malesuada lobortis. Sed quis tellus id nulla mollis iaculis. Nam nec auctor arcu. Aenean molestie lacus ut urna accumsan, a rhoncus orci rhoncus. Fusce orci velit, euismod quis pulvinar ac, ultrices vel dui. Praesent commodo, odio eu ullamcorper eleifend, magna metus euismod elit, in porttitor urna nisl ut nulla. Donec accumsan egestas nulla, ut sollicitudin nulla lacinia ac. Pellentesque felis est, tincidunt et suscipit id, rutrum at odio. Sed fringilla porttitor ipsum. Morbi cursus massa eget arcu hendrerit eleifend. Morbi sit amet.</p>
  <span class="footer-url">www.copperlantern-learn.net</span>
  <span class="page-no">5</span>
</section>

<!-- 6 break section -->
<section class="slide col-c row-2">
  <div class="photo cool" style="inset:0" role="img" aria-label="Bright modern office with desks and pendant lamps, tinted blue"></div>
  <h2 style="left:47px;top:72px;font-size:21px;font-weight:500;line-height:1.18">
    <span style="color:var(--navy)">Break</span><br><span style="color:#fff">Section</span><br><span style="color:#fff">Slide</span>
  </h2>
</section>

<!-- 7 introduction & objectives -->
<section class="slide col-a row-3 bg-navy on-dark">
  <span class="brand-tag on-dark">Copper Lantern</span>
  <h2 class="slide-title" style="left:31px;top:35px;font-size:11.5px;color:var(--sky-soft)">Introduction<br>and Learning<br>Objectives</h2>
  <p class="lorem" style="left:31px;top:88px;width:103px">Lorem ipsum dolor sit amet, consectetur adipiscing elit. Fusce diam tortor, mattis quis dapibus vitae, euismod non purus. Maecenas ut lacus nec mauris feugiat tristique et in metus.</p>
  <p class="sub-label" style="left:31px;top:120px;color:#fff;font-size:3.8px">Subtitle Example</p>
  <p class="lorem" style="left:31px;top:128px;width:103px">Lorem ipsum dolor sit amet, consectetur adipiscing elit. Fusce diam tortor, mattis quis dapibus vitae, euismod non purus. Maecenas ut lacus nec mauris feugiat tristique et in metus. Duis congue eros vel lectus semper semper. Nullam finibus nisl ut ligula vestibulum, ut semper ex suscipit.</p>
  <div class="obj-cell" style="left:170px;top:29px"><div class="n">1</div><p class="sub-label">Subtitle example here</p><p class="lorem">Lorem ipsum dolor sit amet, consectetur adipiscing elit.</p></div>
  <div class="obj-cell" style="left:253px;top:29px"><div class="n">2</div><p class="sub-label">Subtitle example here</p><p class="lorem">Lorem ipsum dolor sit amet, consectetur adipiscing elit.</p></div>
  <div class="obj-cell" style="left:170px;top:82px"><div class="n">3</div><p class="sub-label">Subtitle example here</p><p class="lorem">Lorem ipsum dolor sit amet, consectetur adipiscing elit.</p></div>
  <div class="obj-cell" style="left:253px;top:82px"><div class="n">4</div><p class="sub-label">Subtitle example here</p><p class="lorem">Lorem ipsum dolor sit amet, consectetur adipiscing elit.</p></div>
  <div class="obj-cell" style="left:170px;top:135px"><div class="n">5</div><p class="sub-label">Subtitle example here</p><p class="lorem">Lorem ipsum dolor sit amet, consectetur adipiscing elit.</p></div>
  <div class="obj-cell" style="left:253px;top:135px"><div class="n">6</div><p class="sub-label">Subtitle example here</p><p class="lorem">Lorem ipsum dolor sit amet, consectetur adipiscing elit.</p></div>
  <span class="footer-url">www.copperlantern-learn.net</span>
  <span class="page-no">7</span>
</section>

<!-- 8 chapter recaps -->
<section class="slide col-b row-3" style="background:#fff">
  <div style="left:0;top:0;width:97px;height:203px;background:var(--indigo-2)"></div>
  <h2 class="slide-title" style="left:14px;top:75px;font-size:12px;color:#fff">Chapter<br>Recaps</h2>
  <p class="lorem light" style="left:14px;top:117px;width:74px">Lorem ipsum dolor sit amet, consectetur adipiscing elit. Fusce diam tortor, mattis quis dapibus vitae, euismod non purus. Maecenas ut lacus nec mauris feugiat tristique et in metus.</p>
  <div class="photo" style="left:97px;top:0;width:85px;height:203px" role="img" aria-label="Training room with learners at laptops under pendant lamps"></div>
  <span class="brand-tag">Copper Lantern</span>
  <div class="item" style="left:202px;top:50px"><span class="num-dot">1</span><div class="copy"><p class="sub-label">Subtitle example here</p><p class="lorem">Lorem ipsum dolor sit amet, consectetur adipiscing elit. Fusce diam tortor, mattis quis dapibus vitae, euismod non purus. Maecenas ut lacus nec mauris feugiat tristique et in metus.</p></div></div>
  <div class="item" style="left:202px;top:95px"><span class="num-dot">2</span><div class="copy"><p class="sub-label">Subtitle example here</p><p class="lorem">Lorem ipsum dolor sit amet, consectetur adipiscing elit. Fusce diam tortor, mattis quis dapibus vitae, euismod non purus. Maecenas ut lacus nec mauris feugiat tristique et in metus.</p></div></div>
  <div class="item" style="left:202px;top:142px"><span class="num-dot light">3</span><div class="copy"><p class="sub-label" style="color:var(--sky)">Subtitle example here</p><p class="lorem soft">Lorem ipsum dolor sit amet, consectetur adipiscing elit. Fusce diam tortor, mattis quis dapibus vitae, euismod non purus. Maecenas ut lacus nec mauris feugiat tristique et in metus.</p></div></div>
  <span class="page-no">8</span>
</section>

<!-- 9 pro tip emphasis -->
<section class="slide col-c row-3 bg-royal">
  <h2 class="slide-title" style="left:22px;top:36px;font-size:14.5px;color:var(--sky-soft)">Pro Tip<br>Emphasis</h2>
  <p class="sub-label" style="left:22px;top:77px;color:var(--sky-soft);font-weight:400">Subtitle here</p>
  <div class="photo" style="left:78px;top:35px;width:283px;height:168px;border-radius:90px 0 0 0" role="img" aria-label="Learners working at computers in a classroom"></div>
</section>

<!-- 10 important point / pro tip, two items -->
<section class="slide col-a row-4" style="background:var(--paper)">
  <div class="photo" style="left:0;top:0;width:264px;height:101px" role="img" aria-label="IT worker with headphones typing on a laptop"></div>
  <div style="left:264px;top:0;width:97px;height:203px;background:var(--indigo-2)"></div>
  <span class="brand-tag on-dark">Copper Lantern</span>
  <h2 class="slide-title" style="left:274px;top:75px;font-size:9.6px;color:#fff">Important<br>Point/Pro Tip<br>Emphasis</h2>
  <p class="lorem light" style="left:274px;top:112px;width:76px">Lorem ipsum dolor sit amet, consectetur adipiscing elit. Fusce diam tortor, mattis quis dapibus vitae, euismod non purus. Maecenas ut lacus nec mauris feugiat tristique et in metus.</p>
  <div class="item" style="left:21px;top:133px"><span class="num-dot">1</span><div class="copy" style="width:80px"><p class="sub-label">Subtitle example here</p><p class="lorem">Lorem ipsum dolor sit amet, consectetur adipiscing elit. Fusce diam tortor, mattis quis dapibus vitae, euismod non purus.</p></div></div>
  <div class="item" style="left:135px;top:133px"><span class="num-dot light">2</span><div class="copy" style="width:80px"><p class="sub-label" style="color:var(--sky)">Subtitle example here</p><p class="lorem soft">Lorem ipsum dolor sit amet, consectetur adipiscing elit. Fusce diam tortor, mattis quis dapibus vitae, euismod non purus.</p></div></div>
  <span class="footer-url">www.copperlantern-learn.net</span>
</section>

<!-- 11 important point / pro tip, three items -->
<section class="slide col-b row-4" style="background:#fff">
  <div class="item" style="left:28px;top:33px"><span class="num-dot">1</span><div class="copy"><p class="sub-label">Subtitle example here</p><p class="lorem">Lorem ipsum dolor sit amet, consectetur adipiscing elit. Fusce diam tortor, mattis quis dapibus vitae, euismod non purus. Maecenas ut lacus nec mauris feugiat tristique et in metus.</p></div></div>
  <div class="item" style="left:28px;top:78px"><span class="num-dot">2</span><div class="copy"><p class="sub-label">Subtitle example here</p><p class="lorem">Lorem ipsum dolor sit amet, consectetur adipiscing elit. Fusce diam tortor, mattis quis dapibus vitae, euismod non purus. Maecenas ut lacus nec mauris feugiat tristique et in metus.</p></div></div>
  <div class="item" style="left:28px;top:125px"><span class="num-dot light">3</span><div class="copy"><p class="sub-label" style="color:var(--sky)">Subtitle example here</p><p class="lorem soft">Lorem ipsum dolor sit amet, consectetur adipiscing elit. Fusce diam tortor, mattis quis dapibus vitae, euismod non purus. Maecenas ut lacus nec mauris feugiat tristique et in metus.</p></div></div>
  <div class="photo" style="left:203px;top:0;width:61px;height:203px" role="img" aria-label="Overhead view of a developer working at a laptop"></div>
  <div style="left:264px;top:0;width:97px;height:203px;background:var(--indigo)"></div>
  <span class="brand-tag on-dark">Copper Lantern</span>
  <h2 class="slide-title" style="left:276px;top:92px;font-size:9.6px;color:#fff">Important<br>Point/Pro Tip<br>Emphasis</h2>
  <p class="lorem light" style="left:276px;top:130px;width:76px">Lorem ipsum dolor sit amet, consectetur adipiscing elit. Fusce diam tortor, mattis quis dapibus vitae, euismod non purus. Maecenas ut lacus nec mauris feugiat tristique et in metus.</p>
  <span class="footer-url">www.copperlantern-learn.net</span>
</section>

<!-- 12 important point / pro tip, four items -->
<section class="slide col-c row-4" style="background:var(--paper)">
  <div class="photo" style="left:0;top:0;width:263px;height:101px" role="img" aria-label="Two IT professionals working at desktop monitors"></div>
  <div style="left:263px;top:0;width:98px;height:101px;background:var(--indigo-2)"></div>
  <h2 class="slide-title" style="left:273px;top:12px;font-size:9.6px;color:#fff">Important<br>Point/Pro Tip<br>Emphasis</h2>
  <p class="lorem light" style="left:273px;top:47px;width:78px">Lorem ipsum dolor sit amet, consectetur adipiscing elit. Fusce diam tortor, mattis quis dapibus vitae, euismod non purus. Maecenas ut lacus nec mauris feugiat tristique et in metus.</p>
  <div class="obj-cell" style="left:18px;top:108px;width:68px"><span class="num-dot" style="margin:0 auto">1</span><p class="sub-label" style="color:var(--ink);margin:4px 0 2px">Subtitle example here</p><p class="lorem" style="color:var(--ink)">Lorem ipsum dolor sit amet, consectetur adipiscing elit. Fusce diam tortor, mattis quis dapibus vitae, euismod non.</p></div>
  <div class="obj-cell" style="left:91px;top:108px;width:68px"><span class="num-dot" style="margin:0 auto">2</span><p class="sub-label" style="color:var(--ink);margin:4px 0 2px">Subtitle example here</p><p class="lorem" style="color:var(--ink)">Lorem ipsum dolor sit amet, consectetur adipiscing elit. Fusce diam tortor, mattis quis dapibus vitae, euismod non.</p></div>
  <div class="obj-cell" style="left:165px;top:108px;width:68px"><span class="num-dot" style="margin:0 auto;background:var(--royal)">3</span><p class="sub-label" style="color:var(--ink);margin:4px 0 2px">Subtitle example here</p><p class="lorem" style="color:var(--ink)">Lorem ipsum dolor sit amet, consectetur adipiscing elit. Fusce diam tortor, mattis quis dapibus vitae, euismod non.</p></div>
  <div class="obj-cell" style="left:239px;top:108px;width:68px"><span class="num-dot light" style="margin:0 auto">4</span><p class="sub-label" style="color:var(--sky);margin:4px 0 2px">Subtitle example here</p><p class="lorem soft">Lorem ipsum dolor sit amet, consectetur adipiscing elit. Fusce diam tortor, mattis quis dapibus vitae, euismod non.</p></div>
  <span class="footer-url">www.copperlantern-learn.net</span>
  <span class="page-no">12</span>
</section>

<!-- 13 important point photo grid -->
<section class="slide col-a row-5" style="background:#fff">
  <div class="photo" style="left:0;top:0;width:92px;height:203px" role="img" aria-label="IT worker with headphones at a laptop"></div>
  <div class="photo" style="left:93px;top:0;width:91px;height:96px" role="img" aria-label="Developer at a desktop computer"></div>
  <div class="photo" style="left:93px;top:97px;width:91px;height:106px" role="img" aria-label="Learners in a computer training room"></div>
  <span class="brand-tag">Copper Lantern</span>
  <h2 class="slide-title" style="left:223px;top:48px;font-size:9.6px;color:var(--title-blue)">Important Point</h2>
  <p class="lorem" style="left:223px;top:63px;width:102px">Lorem ipsum dolor sit amet, consectetur adipiscing elit. Fusce diam tortor, mattis quis dapibus vitae, euismod non purus. Maecenas ut lacus nec mauris feugiat tristique et in metus. Duis congue eros vel lectus semper semper. Nullam finibus nisl ut ligula vestibulum, ut semper ex suscipit.</p>
  <h3 class="slide-title" style="left:223px;top:118px;font-size:7.4px;color:var(--accent)">Pro Tip Emphasis</h3>
  <p class="lorem soft" style="left:223px;top:130px;width:102px">Lorem ipsum dolor sit amet, consectetur adipiscing elit. Fusce diam tortor, mattis quis dapibus vitae, euismod non purus. Maecenas ut lacus nec mauris feugiat tristique et in metus. Duis congue eros vel lectus semper semper. Nullam finibus nisl ut ligula vestibulum, ut semper ex suscipit.</p>
  <span class="page-no">13</span>
</section>

<!-- 14 important point with side list -->
<section class="slide col-b row-5" style="background:var(--ice-2)">
  <div style="left:0;top:0;width:97px;height:203px;background:var(--sky)"></div>
  <div class="obj-cell" style="left:8px;top:25px"><div class="n" style="color:#fff">1</div><p class="sub-label" style="color:#fff;font-weight:400">Subtitle example here</p><p class="lorem">Lorem ipsum dolor sit amet, consectetur adipiscing elit.</p></div>
  <div class="obj-cell" style="left:8px;top:78px"><div class="n" style="color:#fff">2</div><p class="sub-label" style="color:#fff;font-weight:400">Subtitle example here</p><p class="lorem">Lorem ipsum dolor sit amet, consectetur adipiscing elit.</p></div>
  <div class="obj-cell" style="left:8px;top:133px"><div class="n" style="color:#fff">3</div><p class="sub-label" style="color:#fff;font-weight:400">Subtitle example here</p><p class="lorem">Lorem ipsum dolor sit amet, consectetur adipiscing elit.</p></div>
  <div class="photo" style="left:97px;top:0;width:85px;height:203px" role="img" aria-label="Developer typing on a laptop at a wooden desk"></div>
  <span class="brand-tag">Copper Lantern</span>
  <h2 class="slide-title" style="left:223px;top:48px;font-size:9.6px;color:var(--title-blue)">Important Point</h2>
  <p class="lorem" style="left:223px;top:63px;width:102px">Lorem ipsum dolor sit amet, consectetur adipiscing elit. Fusce diam tortor, mattis quis dapibus vitae, euismod non purus. Maecenas ut lacus nec mauris feugiat tristique et in metus. Duis congue eros vel lectus semper semper. Nullam finibus nisl ut ligula vestibulum, ut semper ex suscipit.</p>
  <h3 class="slide-title" style="left:223px;top:118px;font-size:7.4px;color:var(--accent)">Pro Tip Emphasis</h3>
  <p class="lorem soft" style="left:223px;top:130px;width:102px">Lorem ipsum dolor sit amet, consectetur adipiscing elit. Fusce diam tortor, mattis quis dapibus vitae, euismod non purus. Maecenas ut lacus nec mauris feugiat tristique et in metus. Duis congue eros vel lectus semper semper. Nullam finibus nisl ut ligula vestibulum, ut semper ex suscipit.</p>
  <span class="page-no">14</span>
</section>

<!-- 15 pro tip emphasis panel -->
<section class="slide col-c row-5" style="background:#fff">
  <div style="left:0;top:0;width:97px;height:203px;background:var(--sky)"></div>
  <span style="left:14px;top:38px;font-size:9px;font-weight:500;color:#fff;white-space:nowrap">Copper Lantern</span>
  <h2 class="slide-title" style="left:14px;top:92px;font-size:10px;color:var(--navy)">Pro Tip<br>Emphasis</h2>
  <p class="lorem" style="left:14px;top:118px;width:74px;color:var(--ice)">Lorem ipsum dolor sit amet, consectetur adipiscing elit. Fusce diam tortor, mattis quis dapibus vitae, euismod non purus. Maecenas ut lacus nec mauris feugiat tristique et in metus.</p>
  <div class="photo" style="left:97px;top:0;width:264px;height:101px" role="img" aria-label="Learners at laptops in a training room"></div>
  <div style="left:126px;top:122px;width:100px"><p class="sub-label" style="font-size:3.6px">Subtitle example here</p><p class="lorem" style="font-size:3.4px">Lorem ipsum dolor sit amet, consectetur adipiscing elit vitae diam tortor, mattis.</p></div>
  <div style="left:242px;top:122px;width:100px"><p class="sub-label" style="font-size:3.6px;color:var(--sky)">Subtitle example here</p><p class="lorem soft" style="font-size:3.4px">Lorem ipsum dolor sit amet, consectetur adipiscing elit vitae diam tortor, mattis.</p></div>
  <div style="left:126px;top:156px;width:100px"><p class="sub-label" style="font-size:3.6px">Subtitle example here</p><p class="lorem" style="font-size:3.4px">Lorem ipsum dolor sit amet, consectetur adipiscing elit vitae diam tortor, mattis.</p></div>
  <div style="left:242px;top:156px;width:100px"><p class="sub-label" style="font-size:3.6px;color:var(--sky)">Subtitle example here</p><p class="lorem soft" style="font-size:3.4px">Lorem ipsum dolor sit amet, consectetur adipiscing elit vitae diam tortor, mattis.</p></div>
  <span class="page-no">15</span>
</section>

<!-- 16 warning message -->
<section class="slide col-a row-6">
  <div class="photo warn" style="inset:0" role="img" aria-label="Dim office interior tinted deep blue"></div>
  <h2 class="slide-title" style="left:30px;top:65px;font-size:15.5px;color:var(--sky-soft)">Warning<br>Message</h2>
  <p class="sub-label" style="left:30px;top:105px;color:var(--sky-soft);font-weight:400">Break slide example</p>
  <p class="lorem" style="left:30px;top:113px;width:95px;color:var(--sky-soft)">Lorem ipsum dolor sit amet, consectetur adipiscing elit. In accumsan euismod dolor, at blandit mi volutpat tincidunt. In lacinia sit orci venenatis, non consectetur est bibendum. In vehicula mauris metus. Lorem ipsum dolor.</p>
</section>

<!-- 17 mini quiz -->
<section class="slide col-b row-6 bg-indigo">
  <h2 class="slide-title" style="left:0;width:100%;top:16px;text-align:center;font-size:13px;color:#fff">Mini Quiz Layout</h2>
  <p style="left:0;width:100%;top:34px;text-align:center;font-size:4.4px;color:var(--sky);text-transform:uppercase">Please answer the questions</p>
  <div class="quiz-cell" style="left:30px;top:67px"><span class="n">1</span><div><p class="q">Question</p><p class="lorem">Lorem ipsum dolor sit amet, consectetur adipiscing elit. Fusce diam tortor, mattis quis dapibus</p></div></div>
  <div class="quiz-cell" style="left:139px;top:67px"><span class="n">2</span><div><p class="q">Question</p><p class="lorem">Lorem ipsum dolor sit amet, consectetur adipiscing elit. Fusce diam tortor, mattis quis dapibus</p></div></div>
  <div class="quiz-cell" style="left:248px;top:67px"><span class="n">3</span><div><p class="q">Question</p><p class="lorem">Lorem ipsum dolor sit amet, consectetur adipiscing elit. Fusce diam tortor, mattis quis dapibus</p></div></div>
  <div class="quiz-cell" style="left:30px;top:110px"><span class="n">4</span><div><p class="q">Question</p><p class="lorem">Lorem ipsum dolor sit amet, consectetur adipiscing elit. Fusce diam tortor, mattis quis dapibus</p></div></div>
  <div class="quiz-cell" style="left:139px;top:110px"><span class="n">5</span><div><p class="q">Question</p><p class="lorem">Lorem ipsum dolor sit amet, consectetur adipiscing elit. Fusce diam tortor, mattis quis dapibus</p></div></div>
  <div class="quiz-cell" style="left:248px;top:110px"><span class="n">6</span><div><p class="q">Question</p><p class="lorem">Lorem ipsum dolor sit amet, consectetur adipiscing elit. Fusce diam tortor, mattis quis dapibus</p></div></div>
  <div class="quiz-cell" style="left:30px;top:152px"><span class="n">7</span><div><p class="q">Question</p><p class="lorem">Lorem ipsum dolor sit amet, consectetur adipiscing elit. Fusce diam tortor, mattis quis dapibus</p></div></div>
  <div class="quiz-cell" style="left:139px;top:152px"><span class="n">8</span><div><p class="q">Question</p><p class="lorem">Lorem ipsum dolor sit amet, consectetur adipiscing elit. Fusce diam tortor, mattis quis dapibus</p></div></div>
  <div class="quiz-cell" style="left:248px;top:152px"><span class="n">9</span><div><p class="q">Question</p><p class="lorem">Lorem ipsum dolor sit amet, consectetur adipiscing elit. Fusce diam tortor, mattis quis dapibus</p></div></div>
  <span class="footer-url">www.copperlantern-learn.net</span>
  <span class="page-no" style="color:#fff">17</span>
</section>

<!-- 18 lab exercise intro -->
<section class="slide col-c row-6" style="background:var(--paper)">
  <div style="left:0;top:0;width:97px;height:101px;background:var(--indigo-2)"></div>
  <h2 class="slide-title" style="left:12px;top:11px;font-size:8.4px;color:#fff">Lab<br>Exercise<br>Introduction</h2>
  <p class="lorem light" style="left:12px;top:46px;width:76px">Lorem ipsum dolor sit amet, consectetur adipiscing elit. Fusce diam tortor, mattis quis dapibus vitae, euismod non purus. Maecenas ut lacus nec mauris feugiat tristique et in metus.</p>
  <div class="photo" style="left:97px;top:0;width:264px;height:101px" role="img" aria-label="Learners at laptops in a training room"></div>
  <p class="lorem" style="left:17px;top:121px;width:140px">Lorem ipsum dolor sit amet, consectetur adipiscing elit. Fusce diam tortor, mattis quis dapibus vitae, euismod non purus. Maecenas ut lacus nec mauris feugiat tristique et in metus. Duis congue eros vel lectus semper semper. Nullam finibus nisl ut ligula vestibulum, ut semper ex suscipit. Lorem ipsum dolor sit amet, consectetur adipiscing elit. Fusce diam tortor, mattis quis dapibus vitae, euismod non purus. Maecenas ut lacus nec mauris feugiat tristique et in metus. Duis congue eros vel lectus semper semper.</p>
  <div class="item" style="left:180px;top:116px"><span class="num-dot">1</span><div class="copy" style="width:115px"><p class="sub-label">Subtitle example here</p><p class="lorem">Lorem ipsum dolor sit amet, consectetur adipiscing elit vitae diam tortor, mattis.</p></div></div>
  <div class="item" style="left:180px;top:151px"><span class="num-dot">2</span><div class="copy" style="width:115px"><p class="sub-label">Subtitle example here</p><p class="lorem">Lorem ipsum dolor sit amet, consectetur adipiscing elit vitae diam tortor, mattis.</p></div></div>
  <span class="footer-url">www.copperlantern-learn.net</span>
  <span class="page-no">18</span>
</section>

<!-- 19 data lines chart -->
<section class="slide col-a row-7" style="background:var(--paper)">
  <span class="brand-tag">Copper Lantern</span>
  <h2 class="slide-title" style="left:30px;top:34px;font-size:13px">
    <span style="color:var(--sky-soft)">Data</span><br><span style="color:var(--title-blue)">Lines</span> <span style="color:var(--sky-soft)">Chart</span>
  </h2>
  <p class="sub-label" style="left:30px;top:66px;font-weight:400">Your subtitle here</p>
  <div class="divider" style="left:30px;top:77px;width:105px;background:var(--sky-soft)"></div>
  <p class="lorem" style="left:30px;top:86px;width:105px">Lorem ipsum dolor sit amet, consectetur adipiscing elit. Fusce diam tortor, mattis quis dapibus vitae, euismod non purus. Maecenas ut lacus nec mauris feugiat tristique et in metus. Duis congue eros vel lectus semper semper. Nullam finibus nisl ut ligula vestibulum, ut semper ex suscipit. Lorem ipsum dolor sit amet, consectetur adipiscing elit. Fusce diam tortor, mattis quis dapibus vitae, euismod non purus. Maecenas ut lacus nec mauris feugiat tristique et in metus. Nullam finibus nisl ut ligula vestibulum.</p>
  <svg style="left:172px;top:52px" width="160" height="110" viewBox="0 0 160 110" role="img" aria-label="3D pie chart with four segments">
    <path d="M4,44 A68,36 0 0,0 140,44 L140,58 A68,36 0 0,1 4,58 Z" fill="#1c2f78"/>
    <path d="M72,44 L72,8 A68,36 0 0,1 136,56.3 Z" fill="#1f8fc0"/>
    <path d="M72,44 L28.3,71.6 A68,36 0 0,1 8.1,31.7 Z" fill="#2a4ea8"/>
    <path d="M72,44 L8.1,31.7 A68,36 0 0,1 72,8 Z" fill="#3a6cc0"/>
    <g transform="translate(9,7)">
      <path d="M136,56.3 A68,36 0 0,1 28.3,71.6 L28.3,85.6 A68,36 0 0,0 136,70.3 Z" fill="#1d6fae"/>
      <path d="M72,44 L136,56.3 A68,36 0 0,1 28.3,71.6 Z" fill="#2f9be0"/>
    </g>
  </svg>
  <span class="footer-url">www.copperlantern-learn.net</span>
  <span class="page-no">19</span>
</section>

<!-- 20 data bars -->
<section class="slide col-b row-7" style="background:var(--paper)">
  <span class="brand-tag">Copper Lantern</span>
  <h2 class="slide-title" style="left:31px;top:38px;font-size:13px;color:var(--title-blue)">Data<br>Bars</h2>
  <p class="lorem" style="left:31px;top:67px;width:103px">Lorem ipsum dolor sit amet, consectetur adipiscing elit. Fusce diam tortor, mattis quis dapibus vitae, euismod non purus. Maecenas ut lacus nec mauris feugiat tristique et in metus. Duis congue eros vel lectus semper semper. Nullam finibus nisl ut ligula vestibulum, ut semper ex suscipit.</p>
  <p class="sub-label" style="left:31px;top:117px;font-size:3.6px">Know more about us</p>
  <p class="lorem" style="left:31px;top:125px;width:103px">Lorem ipsum dolor sit amet, consectetur adipiscing elit. Fusce diam tortor, mattis quis dapibus vitae, euismod non purus. Maecenas ut lacus nec mauris feugiat tristique et in metus. Duis congue eros vel lectus semper semper. Nullam finibus nisl ut ligula vestibulum, ut semper ex suscipit.</p>
  <svg style="left:160px;top:40px" width="180" height="145" viewBox="0 0 180 145" role="img" aria-label="Bar chart with four bars">
    <g stroke="#dde1ea" stroke-width=".5">
      <line x1="12" y1="15" x2="175" y2="15"/><line x1="12" y1="43" x2="175" y2="43"/>
      <line x1="12" y1="71" x2="175" y2="71"/><line x1="12" y1="99" x2="175" y2="99"/>
      <line x1="12" y1="128" x2="175" y2="128" stroke="#b9c0d0"/>
    </g>
    <g font-size="3.4" fill="#9aa3bb" font-family="Roboto, sans-serif">
      <text x="2" y="16">40</text><text x="2" y="44">30</text><text x="2" y="72">20</text><text x="2" y="100">10</text>
      <text x="85" y="136">2020</text>
    </g>
    <rect x="16" y="95" width="34" height="33" fill="#1c1d60"/>
    <rect x="55" y="25" width="34" height="103" fill="#8ec4ec"/>
    <rect x="93" y="64" width="34" height="64" fill="#5b8fd6"/>
    <rect x="132" y="43" width="34" height="85" fill="#2d3a8e"/>
  </svg>
  <span class="footer-url">www.copperlantern-learn.net</span>
  <span class="page-no">20</span>
</section>

<!-- 21 deck close out -->
<section class="slide col-c row-7" style="background:var(--indigo)">
  <h2 class="slide-title" style="left:28px;top:42px;font-size:15px;color:#fff">Deck<br>Close<br>Out</h2>
  <div class="photo" style="left:180px;top:0;width:181px;height:203px" role="img" aria-label="IT professional working at a desktop computer"></div>
  <span class="footer-url">www.copperlantern-learn.net</span>
</section>

</main>
</body>
</html>
```